Startup online payment business - Sporting / Golf, Swift Tee payment

Background:
Our business name is "Swift Tee" we provide online payments for golfing services via our website. We currently have a logo used on our website. No other design style has been developed. Our aim is to remove cash payments for service at golf clubs.

Our Key Values:
Quick and easy
Formal and polite
Fun with professional boundary
Mate-ship relationships
100% online digital

What we want from you:
Marketing design to be used on posters and stickers in a retail setting to direct customers to our online payment Chanel.
Design must incorporate attached logo, URL swifttee.com.au and our key values can act as a guide the type of design. We have used color Hex#007672 for logo background. We are open to use other colors.

Target Market(s)

Golf clubs and golf players

Industry/Entity Type

Golf Course

Font styles to use
Sans Serif

Requirements
Must have
• Directions to online payment via URL: swifttee.com.au
Nice to have
• We like the idea of the slogan: No Cash - No worries. Have attached home screen that will be available from URL link. Consideration if using mobile phone in image. Push the online payment and steps 1. Visit swifttee.com 2. Select club 3. Confirm payment
Should not have
• Cartoons

```html
<!DOCTYPE html>
<html lang="en">
<head>
<meta charset="utf-8">
<title>Swift Tee – No Cash? No Worries! Poster</title>
<link href="https://fonts.googleapis.com/css2?family=Bebas+Neue&family=Montserrat:wght@400;500;600&display=swap" rel="stylesheet">
<style>
  :root {
    --page-bg: #e9ebec;
    --frame-white: #ffffff;
    --slate-light: #5a626b;
    --slate-mid: #434b54;
    --slate-dark: #323941;
    --brand-teal: #007672;
    --accent-teal: #12938c;
    --text-light: #ffffff;
  }

  html, body {
    margin: 0;
    padding: 0;
    width: 1200px;
    height: 1000px;
    overflow: hidden;
    background: var(--page-bg);
  }

  .canvas {
    position: relative;
    width: 1200px;
    height: 1000px;
  }

  .poster {
    position: absolute;
    left: 305px;
    top: 25px;
    width: 590px;
    height: 950px;
    background: var(--frame-white);
    box-shadow: 0 6px 24px rgba(0, 0, 0, 0.12);
  }

  .poster__panel {
    position: absolute;
    left: 26px;
    right: 26px;
    top: 36px;
    bottom: 36px;
    background:
      linear-gradient(135deg, rgba(255,255,255,0.05) 0 50%, rgba(0,0,0,0) 50%),
      linear-gradient(165deg, var(--slate-light) 0%, var(--slate-mid) 45%, var(--slate-dark) 100%);
  }

  .brand-block {
    position: absolute;
    left: 50%;
    top: 14px;
    width: 173px;
    height: 200px;
    transform: translateX(-50%);
    background: var(--brand-teal);
    display: flex;
    align-items: center;
    justify-content: center;
  }

  .brand-block__name {
    font-family: "Bebas Neue", sans-serif;
    font-size: 44px;
    line-height: 1;
    letter-spacing: 2px;
    color: var(--text-light);
    margin-top: 6px;
  }

  .line {
    position: absolute;
    left: 0;
    right: 0;
    margin: 0;
    text-align: center;
    line-height: 1;
  }

  .headline {
    font-family: "Montserrat", sans-serif;
    font-weight: 500;
    font-size: 62px;
    letter-spacing: 3px;
    color: var(--text-light);
    top: 260px;
  }

  .headline--accent {
    font-family: "Bebas Neue", sans-serif;
    font-weight: 400;
    font-size: 84px;
    letter-spacing: 3px;
    color: var(--brand-teal);
    top: 330px;
  }

  .step__label {
    font-family: "Bebas Neue", sans-serif;
    font-size: 34px;
    letter-spacing: 1.5px;
    color: var(--text-light);
  }

  .step__text {
    font-family: "Montserrat", sans-serif;
    font-weight: 500;
    font-size: 18px;
    letter-spacing: 1px;
    color: var(--text-light);
  }

  .step-1 .step__label { top: 458px; }
  .step-1 .step__text  { top: 501px; }
  .step-2 .step__label { top: 557px; }
  .step-2 .step__text  { top: 599px; }
  .step-3 .step__label { top: 661px; }
  .step-3 .step__text  { top: 706px; }

  .done {
    font-family: "Bebas Neue", sans-serif;
    font-size: 44px;
    letter-spacing: 1.5px;
    color: var(--brand-teal);
    top: 754px;
  }

  .site-url {
    font-family: "Montserrat", sans-serif;
    font-weight: 500;
    font-size: 24px;
    letter-spacing: 1.5px;
    color: var(--text-light);
    top: 849px;
  }
</style>
</head>
<body>
  <main class="canvas">
    <article class="poster">
      <div class="poster__panel"></div>

      <div class="brand-block">
        <span class="brand-block__name">SWIFT TEE</span>
      </div>

      <h1 class="line headline">NO CASH?</h1>
      <p class="line headline--accent">NO WORRIES!</p>

      <section class="step step-1">
        <p class="line step__label">STEP 1</p>
        <p class="line step__text">Visit swifttee.com</p>
      </section>
      <section class="step step-2">
        <p class="line step__label">STEP 2</p>
        <p class="line step__text">Select your Club</p>
      </section>
      <section class="step step-3">
        <p class="line step__label">STEP 3</p>
        <p class="line step__text">Confirm your Payment</p>
      </section>

      <p class="line done">DONE!</p>

      <p class="line site-url">swifttee.com.au</p>
    </article>
  </main>
</body>
</html>
```